Priority Goals poster for school year

We are an elementary school and the past two years have had you help us to design a "poster" that illustrates our goal of the coming year. I am attaching our last year's one, along with some photos of our (ver rough) thinking for next years. The priority goal at top remains the same. Can't wait to see your genius ideas! :)

Target Market(s)

Staff of an elementary school and parents to some (informative) extent as well.

Colors
296eb1
6094c6
fbed22
fbee3f

Requirements
Must have
• items from the white board picture we have attached

```html
<!DOCTYPE html>
<html lang="en">
<head>
<meta charset="utf-8">
<title>2021 - 2022 Priority Goals – Cedar Ridge Elementary School</title>
<link rel="stylesheet" href="https://fonts.googleapis.com/css2?family=Montserrat:wght@600;700;800&family=Open+Sans:wght@400;600&family=Barlow+Condensed:wght@700&display=swap">
<style>
  :root {
    --navy: #1f3263;
    --blue: #296eb1;
    --blue-soft: #6094c6;
    --yellow: #fbed22;
    --yellow-soft: #fbee3f;
    --amber: #f7b91c;
    --grey-light: #e9eaec;
    --grey-mid: #c9cbcf;
    --white: #ffffff;
  }
  * { box-sizing: border-box; margin: 0; padding: 0; }
  html, body { width: 848px; height: 1200px; overflow: hidden; background: var(--white); }
  .poster {
    position: relative; width: 848px; height: 1200px; overflow: hidden;
    background: var(--white); font-family: "Open Sans", Arial, sans-serif;
  }
  .backdrop {
    position: absolute; left: 0; top: 171px; width: 848px; height: 925px;
    background: radial-gradient(ellipse at 50% 45%, var(--grey-light) 0%, var(--grey-mid) 60%, var(--grey-light) 100%);
  }
  .page-title {
    position: absolute; left: 44px; top: 48px;
    font-family: "Montserrat", Arial, sans-serif; font-weight: 700; font-size: 35px;
    color: var(--navy); letter-spacing: 0.2px;
  }
  .page-title .accent { color: var(--blue); }
  .goal-banner {
    position: absolute; left: 0; top: 107px; width: 630px; height: 84px;
    background: var(--blue);
    clip-path: polygon(0 0, 94% 0, 100% 50%, 94% 100%, 0 100%);
    color: var(--white); font-family: "Montserrat", Arial, sans-serif; font-weight: 700;
    font-size: 19px; line-height: 27px; padding: 16px 0 0 30px;
  }
  .school-mark {
    position: absolute; right: 34px; top: 26px; width: 168px;
    display: flex; flex-direction: column; align-items: center; gap: 8px;
    font-family: "Montserrat", Arial, sans-serif; font-weight: 800; color: var(--navy);
    text-align: center; font-size: 15px; line-height: 17px;
  }
  .school-mark .dot { width: 66px; height: 66px; border-radius: 50%; background: var(--yellow); }
  .ribbons { position: absolute; left: 0; top: 0; }
  .ribbon-text { font-family: "Open Sans", Arial, sans-serif; font-size: 16px; fill: #1b1b1b; }
  .ribbon-text.large { font-size: 25px; }
  .big-picture {
    position: absolute; left: 213px; top: 560px; width: 400px; text-align: center;
    font-family: "Montserrat", Arial, sans-serif; font-weight: 800; color: var(--white);
  }
  .big-picture .headline { font-size: 42px; line-height: 50px; }
  .big-picture .year { font-size: 40px; line-height: 52px; font-weight: 700; }
  .foundations {
    position: absolute; left: 43px; top: 1020px; width: 790px;
    font-family: "Barlow Condensed", "Arial Narrow", sans-serif; font-weight: 700;
    font-size: 50px; color: var(--navy); letter-spacing: 0.6px; white-space: nowrap;
  }
  .rule { position: absolute; left: 0; top: 1086px; width: 848px; height: 8px; background: var(--yellow); }
  .site-footer {
    position: absolute; left: 0; top: 1094px; width: 848px; height: 106px; background: var(--navy);
    color: var(--white); font-size: 15px; font-weight: 600;
  }
  .contact { position: absolute; left: 34px; display: flex; align-items: center; gap: 12px; }
  .contact.address { top: 28px; }
  .contact.phone { top: 58px; }
  .social { position: absolute; right: 34px; top: 63px; display: flex; align-items: center; gap: 9px; }
  .social .box { width: 17px; height: 17px; border: 2px solid var(--white); border-radius: 4px; }
</style>
</head>
<body>
<main class="poster">
  <div class="backdrop"></div>

  <h1 class="page-title">2021 - 2022 <span class="accent">PRIORITY GOALS</span></h1>

  <div class="goal-banner">We WILL accelerate the academic &amp; social / emotional<br>growth of the students we served by :</div>

  <div class="school-mark">
    <span class="dot"></span>
    <span>CEDAR RIDGE<br>ELEMENTARY SCHOOL</span>
  </div>

  <svg class="ribbons" width="848" height="1200" viewBox="0 0 848 1200" aria-hidden="true">
    <defs>
      <linearGradient id="ribbon-fill" x1="0" y1="0" x2="1" y2="0">
        <stop offset="0" stop-color="var(--yellow)"/>
        <stop offset="0.7" stop-color="var(--yellow-soft)"/>
        <stop offset="1" stop-color="var(--amber)"/>
      </linearGradient>
      <path id="r1" d="M36 577 A400 400 0 0 1 306 271"/>
      <path id="r2" d="M93 556 A380 380 0 0 1 392 285"/>
      <path id="r3" d="M178 534 A400 400 0 0 1 541 356"/>
      <path id="r4" d="M285 505 A520 520 0 0 1 790 392"/>
      <path id="r5" d="M385 522 A900 900 0 0 1 762 490"/>
      <path id="r6" d="M7 727 A1200 1200 0 0 0 463 745"/>
      <path id="r7" d="M93 826 A700 700 0 0 0 556 741"/>
      <path id="r8" d="M242 884 A600 600 0 0 0 641 727"/>
      <path id="r9" d="M370 940 A500 500 0 0 0 727 712"/>
      <path id="r10" d="M506 969 A450 450 0 0 0 805 670"/>
    </defs>

    <g fill="none" stroke="var(--blue)" stroke-width="34">
      <path d="M60 600 A420 420 0 0 1 330 262" transform="translate(14 10)"/>
      <path d="M420 380 A460 460 0 0 1 720 330"/>
      <path d="M470 480 A700 700 0 0 1 800 460" transform="translate(0 14)"/>
      <path d="M30 760 A900 900 0 0 0 480 770" transform="translate(6 16)"/>
      <path d="M300 960 A520 520 0 0 0 700 760" transform="translate(-20 24)"/>
      <path d="M540 1000 A470 470 0 0 0 830 700" transform="translate(8 18)"/>
    </g>

    <circle cx="413" cy="600" r="195" fill="var(--blue)"/>
    <circle cx="413" cy="600" r="150" fill="none" stroke="var(--blue-soft)" stroke-width="6" opacity="0.5"/>

    <g fill="none" stroke="url(#ribbon-fill)" stroke-width="40">
      <use href="#r1"/><use href="#r2"/><use href="#r3"/><use href="#r4"/><use href="#r5"/>
      <use href="#r6"/><use href="#r7"/><use href="#r8"/>
      <use href="#r9" stroke-width="52"/><use href="#r10"/>
    </g>

    <text class="ribbon-text" dy="6"><textPath href="#r1" startOffset="3%">Celebrate &amp; Build on 4 years of Success - Our Promise</textPath></text>
    <text class="ribbon-text" dy="6"><textPath href="#r2" startOffset="3%">Know who we are and where we are going;  Voices of All</textPath></text>
    <text class="ribbon-text" dy="6"><textPath href="#r3" startOffset="4%">Do what we ♡ love   Teach kids for proven growth</textPath></text>
    <text class="ribbon-text" dy="6"><textPath href="#r4" startOffset="2%">Clear, clarified expectations   permissions / support to act</textPath></text>
    <text class="ribbon-text" dy="6"><textPath href="#r5" startOffset="4%">Communicate! Be intentional with plans / actions</textPath></text>
    <text class="ribbon-text" dy="6"><textPath href="#r6" startOffset="4%">Use expertise   Use what we have learned</textPath></text>
    <text class="ribbon-text" dy="6"><textPath href="#r7" startOffset="6%">New Beginnings ? lots of new experiences ahead</textPath></text>
    <text class="ribbon-text" dy="6"><textPath href="#r8" startOffset="6%">SEL / Mental Health for all / Connect / ♥ Smile  Laugh</textPath></text>
    <text class="ribbon-text large" dy="8"><textPath href="#r9" startOffset="10%">Partnership big / small</textPath></text>
    <text class="ribbon-text" dy="6"><textPath href="#r10" startOffset="6%">Stable / Predictable / Consistent (=Strong)</textPath></text>
  </svg>

  <div class="big-picture">
    <div class="headline">THE BIG PICTURE</div>
    <div class="year">2021 - 2022</div>
  </div>

  <h2 class="foundations">FOUNDATIONAL BELIEFS AND PROMISES</h2>
  <div class="rule"></div>

  <footer class="site-footer">
    <div class="contact address">
      <svg width="16" height="18" viewBox="0 0 16 18" aria-hidden="true"><path d="M8 1a6 6 0 0 0-6 6c0 4.5 6 10 6 10s6-5.5 6-10a6 6 0 0 0-6-6z" fill="none" stroke="#fff" stroke-width="1.8"/><circle cx="8" cy="7" r="2.2" fill="#fff"/></svg>
      <span>1180 Alder Creek Rd., Brookfield, WA 98000</span>
    </div>
    <div class="contact phone">
      <svg width="16" height="16" viewBox="0 0 16 16" aria-hidden="true"><path d="M4 1.5l2.2 3-1.4 1.6a8 8 0 0 0 5.1 5.1l1.6-1.4 3 2.2-1.3 2.3C7 14.5 1.5 9 1.7 2.8z" fill="none" stroke="#fff" stroke-width="1.6" stroke-linejoin="round"/></svg>
      <span>555-201-4470</span>
    </div>
    <div class="social"><span class="box"></span><span>@cedarridgelearner</span></div>
  </footer>
</main>
</body>
</html>
```